Visitenkarte erstellen für Reiki Praxis

Visitenkarten für Reiki Praxis Doppelseitig

business cards reiki practice double-sided

The background can also be a different color

```html
<!DOCTYPE html>
<html lang="en">
<head>
<meta charset="utf-8">
<title>Lumen Reiki – Business Cards</title>
<link href="https://fonts.googleapis.com/css2?family=Open+Sans:wght@400&family=Arimo:wght@400;700&display=swap" rel="stylesheet">
<style>
  :root {
    --stage: #5b5b5b;
    --card: #000000;
    --edge: #a84f7f;
    --rose: #b05585;
    --white: #ffffff;
    --muted: #e8e8e8;
  }
  * { box-sizing: border-box; margin: 0; padding: 0; }
  html, body { width: 1200px; height: 810px; overflow: hidden; }
  body {
    background: var(--stage);
    display: flex;
    flex-direction: column;
    align-items: center;
    justify-content: center;
    gap: 40px;
    font-family: "Arimo", Arial, sans-serif;
  }
  .card {
    position: relative;
    width: 600px;
    height: 343px;
    background: var(--card);
    border-bottom: 6px solid var(--edge);
    box-shadow: 0 12px 30px rgba(0,0,0,0.45);
    color: var(--white);
  }
  .wordmark {
    display: flex;
    align-items: center;
    gap: 12px;
    font-family: "Open Sans", Arial, sans-serif;
    font-weight: 400;
    color: var(--white);
    letter-spacing: 0.06em;
    text-transform: uppercase;
    white-space: nowrap;
  }
  .wordmark__dot {
    border-radius: 50%;
    background: var(--white);
  }

  /* Info side */
  .card--info .wordmark {
    position: absolute;
    top: 46px;
    right: 40px;
    font-size: 26px;
  }
  .card--info .wordmark__dot { width: 12px; height: 12px; }
  .address {
    position: absolute;
    top: 118px;
    right: 40px;
    text-align: right;
    font-size: 12px;
    line-height: 1.4;
    color: var(--muted);
  }
  .person {
    position: absolute;
    left: 44px;
    top: 168px;
  }
  .person__name {
    font-weight: 700;
    font-size: 22px;
    color: var(--rose);
    text-transform: uppercase;
    letter-spacing: 0.01em;
  }
  .person__role {
    font-size: 13px;
    text-transform: uppercase;
    margin-top: 2px;
  }
  .contacts {
    list-style: none;
    margin-top: 18px;
    display: flex;
    flex-direction: column;
    gap: 8px;
    font-size: 13px;
  }
  .contacts li { display: flex; align-items: center; gap: 12px; }
  .contacts svg { width: 18px; height: 18px; flex: none; }
  .contacts .accent { color: var(--rose); }

  /* Front side */
  .card--front {
    display: flex;
    align-items: center;
    justify-content: center;
  }
  .card--front .wordmark { font-size: 44px; gap: 18px; }
  .card--front .wordmark__dot { width: 18px; height: 18px; }
</style>
</head>
<body>
  <section class="card card--info" aria-label="Business card, contact side">
    <div class="wordmark"><span class="wordmark__dot"></span>Lumen Reiki</div>
    <p class="address">2270 Alder Lane, Brookfield,<br>CA 90000</p>
    <div class="person">
      <h1 class="person__name">Dr. Clara Benning</h1>
      <p class="person__role">Audiologist</p>
      <ul class="contacts">
        <li>
          <svg viewBox="0 0 24 24" aria-hidden="true"><path fill="var(--rose)" d="M6.6 10.8a15 15 0 0 0 6.6 6.6l2.2-2.2a1 1 0 0 1 1-.25 11.4 11.4 0 0 0 3.6.57 1 1 0 0 1 1 1V20a1 1 0 0 1-1 1A17 17 0 0 1 3 4a1 1 0 0 1 1-1h3.5a1 1 0 0 1 1 1c0 1.25.2 2.45.57 3.57a1 1 0 0 1-.25 1z"/></svg>
          555-014-2290
        </li>
        <li>
          <svg viewBox="0 0 24 24" aria-hidden="true"><rect x="2" y="5" width="20" height="14" rx="1.5" fill="var(--rose)"/><path d="M3 6l9 7 9-7" fill="none" stroke="#000" stroke-width="1.6"/></svg>
          info@youremail.com
        </li>
        <li>
          <svg viewBox="0 0 24 24" aria-hidden="true"><g fill="none" stroke="var(--rose)" stroke-width="1.6"><circle cx="12" cy="12" r="9"/><ellipse cx="12" cy="12" rx="4" ry="9"/><path d="M3 12h18M5 7h14M5 17h14"/></g></svg>
          <span>www.<span class="accent">yourwebsite</span>.com</span>
        </li>
      </ul>
    </div>
  </section>

  <section class="card card--front" aria-label="Business card, front side">
    <div class="wordmark"><span class="wordmark__dot"></span>Lumen Reiki</div>
  </section>
</body>
</html>
```